Property Development Business Cards

I need a business card design for Blue Harbour Developments Pty Ltd. We are a property development company in Australia and our name defines the five values that we adhere to, being Profitable, Partnerships, Quality Developments, Eco Friendly and Enduring Design.

I have attached the current logo that I use, it is just five yellow circles connected to a single cricle in the middle.

Target Market(s)

Our Target audience is real estate agents, owners of properties, builders and other trades

Industry/Entity Type

Business

Requirements
Must have
• Want to have two sides to the card, one with details and one to just highlight the company

```html
<!DOCTYPE html>
<html lang="en">
<head>
<meta charset="utf-8">
<title>Blue Harbour Developments – Business Card</title>
<link href="https://fonts.googleapis.com/css2?family=Arimo:wght@400;700&display=swap" rel="stylesheet">
<style>
  :root {
    --page: #ffffff;
    --card: #ffffff;
    --card-edge: #d9d9d9;
    --brand-blue: #1d5fa6;
    --text-blue: #2266ad;
    --mark: #f4bd35;
  }
  html, body {
    margin: 0;
    padding: 0;
    width: 1200px;
    height: 331px;
    overflow: hidden;
    background: var(--page);
    font-family: "Arimo", Arial, sans-serif;
  }
  .canvas {
    position: relative;
    width: 1200px;
    height: 331px;
  }
  .card {
    position: absolute;
    top: 10px;
    height: 316px;
    background: var(--card);
    border: 1px solid var(--card-edge);
    box-shadow: 1px 2px 3px rgba(0,0,0,0.12);
    box-sizing: border-box;
  }
  .card--front { left: 9px; width: 568px; }
  .card--back  { left: 629px; width: 566px; }

  .brand-mark {
    position: absolute;
    border-radius: 50%;
    background: var(--mark);
  }
  .card--front .brand-mark {
    left: 239px;
    top: 78px;
    width: 90px;
    height: 90px;
  }
  .company-name {
    position: absolute;
    left: 0;
    right: 0;
    top: 270px;
    text-align: center;
    color: var(--brand-blue);
    font-size: 21px;
    font-weight: 400;
  }

  .back-brand {
    position: absolute;
    right: 22px;
    top: 34px;
    display: flex;
    align-items: center;
    gap: 8px;
  }
  .back-brand .brand-mark {
    position: static;
    width: 30px;
    height: 30px;
  }
  .back-brand__name {
    color: var(--brand-blue);
    font-size: 13px;
    font-weight: 400;
  }

  .contact {
    position: absolute;
    left: 22px;
    top: 88px;
    color: var(--text-blue);
  }
  .contact__name {
    margin: 0 0 38px;
    font-size: 26px;
    line-height: 30px;
    font-weight: 700;
  }
  .contact__lines {
    margin: 0;
    font-size: 16.5px;
    line-height: 22.6px;
    font-style: normal;
  }
  .contact__web {
    margin: 26px 0 0;
    font-size: 16.5px;
    line-height: 22px;
  }
</style>
</head>
<body>
<div class="canvas">
  <section class="card card--front">
    <div class="brand-mark" aria-hidden="true"></div>
    <div class="company-name">Blue Harbour Developments Pty Ltd</div>
  </section>

  <section class="card card--back">
    <div class="back-brand">
      <div class="brand-mark" aria-hidden="true"></div>
      <span class="back-brand__name">Blue Harbour Developments</span>
    </div>
    <div class="contact">
      <h1 class="contact__name">Daniel Marsh</h1>
      <address class="contact__lines">
        Mobile: 0400.518.263<br>
        Email: Daniel@BlueHarbourDevelopments.com.au<br>
        P.O. Box 218<br>
        Hartwell, ACT 2906
      </address>
      <p class="contact__web">www.BlueHarbourDevelopments.com.au</p>
    </div>
  </section>
</div>
</body>
</html>
```